Our company needs a new modern concept for our webstore

Brindel Supplier Group is a product supply company supplying product for the building, architecture, interior design, printing and signage industries. We are looking for a clean, modern, corporate and sophisticated new look for our webstore.
The webstore should be PageForge and Ravo Basket based.
The webstore should include subtle and professional animations to enhance the look and catch the eye.
The Quince webstore is a good example to follow. We love the clean and simple yet highly sophisticated look of the Quince site. The homepage should start with a hero image at the top involving cladding and aluminium signage for corporate branding.
Underneath the hero image there should be a few lines of copy discussion the quality of our products (we will create the actual copy).
As the user scrolls past the few lines of copy they should come to our product categories represented by good quality end use images.
The product categories will be as follows:
Aluminium Panel – Ox Panel
Aluminium Composite Panel – Murt Panel
Acrylic Sheets – Temvoro
Print and Display
LED Lighting – Vesko LED Lighting
The brand logo for each of these product categories are attached to this brief. The logos should be used in the product categories in a clean, subtle but clear way.
There should be some subtle animation built into the product categories, such as the images expanding when hovering over or the logos animating onto the background images.

The home page navigation bar should appear at the very top above the hero image and should have the following buttons:
Home page
About page
Projects Gallery page
News
Contact page
Our main company logo Brindel Supplier Group is attached to this brief and should be shown small but clear at the top of the page either next to the navigation bar or in the middle of it.
The phone number 1300 458 903 should also be clearly shown at the top of the webstore.

For examples of the kinds of websites we like and level of clean, modern professionalism, see the links below:
https://www.quincegoods.example/store
https://www.plinthmedia.example.au/
https://www.corvanbuildworks.example.au/
https://tkrexteriors.example.au/

Industry/Entity Type

Architecture, Interior Design, Building, Shop fitting

Number of Pages Required

3 page

Font styles to use
Serif
Sans Serif

Requirements
Must have
• A clean, upmarket, modern and professional look that will appeal to architects and interior designers.
Nice to have
• An outstanding and slick website that promotes us as industry leaders for our products
Should not have
• A low market and cheap look that does not reflect the brand identify or its level of sophistication.

```html
<!DOCTYPE html>
<html lang="en">
<head>
<meta charset="utf-8">
<title>Brindel Supplier Group</title>
<link href="https://fonts.googleapis.com/css2?family=Poppins:wght@400;500;600;700&family=Montserrat:wght@400;500;600&display=swap" rel="stylesheet">
<style>
:root{
  --maroon:#6b1141;
  --maroon-dark:#55102f;
  --ink:#111114;
  --night:#141417;
  --text:#222;
  --muted:#6d6d6d;
  --white:#fff;
  --line:#d9d9d9;
}
*{margin:0;padding:0;box-sizing:border-box}
html,body{width:1200px;height:3800px;overflow:hidden}
body{position:relative;background:var(--white);font-family:"Montserrat",sans-serif;color:var(--text)}
.abs{position:absolute}
.heading{font-family:"Poppins",sans-serif}
.fill{display:block}
.btn{position:absolute;display:flex;align-items:center;justify-content:center;font-family:"Montserrat",sans-serif;font-size:11px;font-weight:500;text-transform:uppercase;text-decoration:none}
.btn-solid{background:var(--maroon);color:var(--white)}
.btn-outline{border:1px solid #555;color:var(--text);background:var(--white)}

/* header */
.site-header{position:absolute;left:0;top:0;width:1200px;height:83px;background:var(--white)}
.brand{position:absolute;left:89px;top:18px;width:120px;font-family:"Poppins",sans-serif;font-weight:700;font-size:20px;line-height:22px;color:var(--maroon)}
.brand span{display:block;font-size:10px;font-weight:600;letter-spacing:.6px;line-height:14px;text-transform:uppercase}
.nav a{position:absolute;top:33px;font-family:"Poppins",sans-serif;font-size:13px;font-weight:500;color:var(--ink);text-decoration:none}
.nav a.active{color:var(--maroon);border-bottom:1px solid var(--maroon);padding-bottom:1px}
.phone-box{position:absolute;left:837px;top:25px;width:31px;height:31px;border:1px solid #999;border-radius:3px}
.phone-label{position:absolute;left:875px;top:26px;font-size:11px;color:var(--muted)}
.phone-num{position:absolute;left:875px;top:40px;font-size:13px;font-weight:600;color:var(--ink)}
.inquire{left:983px;top:25px;width:128px;height:33px;font-family:"Poppins",sans-serif;font-size:14px;font-weight:600;text-transform:none}

/* hero */
.hero-card{position:absolute;left:89px;top:100px;width:1022px;height:423px;background:var(--white);box-shadow:0 8px 24px rgba(0,0,0,.15)}
.hero-title{position:absolute;left:30px;top:40px;width:280px;font-family:"Poppins",sans-serif;font-weight:700;font-size:37px;line-height:42px;color:var(--ink)}
.hero-copy{position:absolute;left:30px;top:218px;width:270px;font-size:12.5px;line-height:20px;color:var(--muted)}
.dots{position:absolute;left:38px;top:375px;display:flex;gap:8px}
.dots span{width:10px;height:10px;border:1px solid #555;border-radius:50%}
.dots span.on{background:var(--maroon);border-color:var(--maroon)}

/* about */
.section-title{font-family:"Poppins",sans-serif;font-weight:600;font-size:29px;color:var(--maroon)}
.about-lead{position:absolute;left:614px;top:736px;width:400px;font-size:12.5px;font-weight:600;line-height:19px;color:var(--ink)}
.about-copy{position:absolute;left:614px;top:792px;width:470px;font-size:12.5px;line-height:19px;color:#333}
.about-copy p{margin-bottom:18px}

/* products */
.tile{position:absolute;overflow:hidden;border:2px solid #cfcfcf}
.tile-card{position:absolute;background:var(--white);display:flex;flex-direction:column;align-items:center;justify-content:center;text-align:center}
.tile-brand{font-family:"Poppins",sans-serif;font-weight:600;font-size:30px;letter-spacing:2px;color:var(--ink);display:flex;align-items:center;gap:12px}
.tile-brand i{display:inline-block;width:14px;height:14px;background:var(--ink)}
.tile-sub{font-family:"Poppins",sans-serif;font-weight:600;font-size:16px;color:var(--maroon);margin-top:8px}
.tile-copy{font-size:12.5px;line-height:18px;color:#555;width:260px;margin-top:6px}
.tile-name{font-family:"Poppins",sans-serif;font-weight:500;font-size:21px;color:var(--ink)}

/* gallery */
.gallery-card{position:absolute;width:324px;height:291px;border:2px solid var(--maroon);overflow:hidden}
.gallery-cap{position:absolute;left:0;right:0;bottom:10px;text-align:center;font-family:"Poppins",sans-serif;font-size:16px;color:var(--white)}

/* news */
.news-card{position:absolute;top:2765px;width:324px;height:360px;background:var(--white)}
.news-date{position:absolute;left:20px;top:218px;font-family:"Poppins",sans-serif;font-weight:600;font-size:26px;color:var(--maroon);line-height:26px}
.news-date small{display:block;font-family:"Montserrat",sans-serif;font-weight:400;font-size:10px;color:#333;line-height:14px}
.news-title{position:absolute;left:85px;top:211px;width:220px;font-family:"Poppins",sans-serif;font-weight:600;font-size:15px;line-height:18px;color:var(--maroon)}
.news-copy{position:absolute;left:85px;top:256px;width:220px;font-size:11.5px;line-height:18px;color:#444}

/* newsletter */
.nl-title{position:absolute;left:263px;top:3330px;font-family:"Poppins",sans-serif;font-weight:600;font-size:17px;color:var(--maroon)}
.nl-copy{position:absolute;left:263px;top:3356px;width:310px;font-size:13px;line-height:19px;color:#333}
.nl-form{position:absolute;left:617px;top:3346px;width:416px;height:36px;border:1px solid #bbb;background:var(--white)}
.nl-form span{position:absolute;left:13px;top:10px;font-size:12px;color:#999}

/* footer */
.site-footer{position:absolute;left:0;top:3451px;width:1200px;height:306px;background:var(--ink)}
.foot-brand{position:absolute;left:89px;top:150px;width:170px;font-family:"Poppins",sans-serif;font-weight:700;font-size:30px;line-height:32px;color:var(--maroon)}
.foot-brand span{display:block;font-size:13px;letter-spacing:1.5px;line-height:20px;text-transform:uppercase}
.foot-head{position:absolute;top:80px;font-family:"Poppins",sans-serif;font-weight:600;font-size:15px;color:var(--maroon)}
.foot-links a{position:absolute;left:353px;font-size:12px;color:#eee;text-decoration:none}
.foot-links a.active{color:var(--maroon)}
.foot-info{position:absolute;left:599px;font-size:12.5px;line-height:19px;color:#eee}
.copyright{position:absolute;left:89px;top:3771px;font-size:12px;color:#222}
.social{position:absolute;top:3770px;width:19px;height:19px;border-radius:50%;background:var(--maroon)}
</style>
</head>
<body>

<!-- header -->
<header class="site-header">
  <div class="brand">Brindel<span>Supplier Group</span></div>
  <nav class="nav">
    <a href="#" class="active" style="left:347px">Home</a>
    <a href="#" style="left:419px">About Us</a>
    <a href="#" style="left:512px">Projects Gallery</a>
    <a href="#" style="left:644px">News</a>
    <a href="#" style="left:713px">Contact Us</a>
  </nav>
  <div class="phone-box">
    <svg width="29" height="29" viewBox="0 0 29 29"><path d="M10 8c1 0 2 3 2 4s-1.5 1-1 2.5 2.5 3.5 3.5 3.5 1.2-1 2-1 3.5 1 3.5 2-1 2.5-2.5 2.5C12 21.5 7.5 16.5 7.5 11 7.5 9.3 8.8 8 10 8z" fill="#6b1141"/></svg>
  </div>
  <div class="phone-label">Phone</div>
  <div class="phone-num">1300 458 903</div>
  <a class="btn btn-solid inquire">Inquire Now</a>
</header>

<!-- hero band -->
<svg class="abs" style="left:0;top:83px" width="1200" height="400"><defs><linearGradient id="band1" x1="0" y1="0" x2="1" y2="1"><stop offset="0" stop-color="#1d1d21"/><stop offset="1" stop-color="#0f0f12"/></linearGradient></defs><polygon points="0,0 1200,0 1200,316 0,389" fill="url(#band1)"/></svg>
<section class="hero-card">
  <h1 class="hero-title">The way of The Future for Aluminium Panels</h1>
  <p class="hero-copy">Lorem Ipsum is simply dummy text of the printing and typesetting industry. Lorem Ipsum has been...</p>
  <a class="btn btn-solid" style="left:28px;top:301px;width:116px;height:32px">Read More</a>
  <div class="dots"><span class="on"></span><span></span><span></span></div>
  <svg class="abs" style="left:335px;top:0" width="687" height="423" role="img" aria-label="Modern glass and aluminium clad office building with landscaped forecourt">
    <defs><linearGradient id="heroG" x1="0" y1="0" x2="0" y2="1"><stop offset="0" stop-color="#1f5fd0"/><stop offset=".25" stop-color="#5b98e2"/><stop offset=".45" stop-color="#c9d6df"/><stop offset=".7" stop-color="#8fa3ad"/><stop offset=".85" stop-color="#6f8a62"/><stop offset="1" stop-color="#3f6a2c"/></linearGradient></defs>
    <rect width="687" height="423" fill="url(#heroG)"/>
  </svg>
</section>

<!-- about -->
<div class="abs" style="left:89px;top:714px;width:367px;height:313px;background:var(--maroon)"></div>
<svg class="abs" style="left:103px;top:627px" width="433" height="386" role="img" aria-label="Boutique shop interior with chrome pipe fit-out and mannequins">
  <defs><linearGradient id="aboutG" x1="0" y1="0" x2="1" y2="1"><stop offset="0" stop-color="#15151a"/><stop offset=".35" stop-color="#55565c"/><stop offset=".6" stop-color="#8a8b90"/><stop offset="1" stop-color="#25252a"/></linearGradient></defs>
  <rect width="433" height="386" fill="url(#aboutG)"/>
</svg>
<h2 class="section-title abs" style="left:614px;top:676px">ABOUT US</h2>
<p class="about-lead">Lorem Ipsum is simply dummy text of the printing and typesetting industry.</p>
<div class="about-copy">
  <p>Lorem Ipsum has been the industry's standard dummy text ever since the 1500s, when an unknown printer took a galley of type and scrambled it to make a type specimen book.</p>
  <p>It has survived not only five centuries, but also the leap into electronic typesetting, remaining essentially unchanged.</p>
</div>
<a class="btn btn-outline" style="left:614px;top:934px;width:115px;height:33px">Read More</a>

<!-- products -->
<svg class="abs" style="left:0;top:1085px" width="1200" height="952"><defs><linearGradient id="band2" x1="0" y1="0" x2="1" y2="1"><stop offset="0" stop-color="#1b1b1f"/><stop offset="1" stop-color="#0e0e11"/></linearGradient></defs><polygon points="0,63 1200,0 1200,885 0,952" fill="url(#band2)"/></svg>
<section aria-label="Product categories">
  <div class="tile" style="left:89px;top:1209px;width:318px;height:357px">
    <svg class="fill" width="318" height="357" role="img" aria-label="Curved aluminium panel facade against pale sky"><defs><linearGradient id="t1" x1="0" y1="0" x2="1" y2=".3"><stop offset="0" stop-color="#6f7b88"/><stop offset=".3" stop-color="#b9c3cc"/><stop offset=".55" stop-color="#eef1f4"/><stop offset=".8" stop-color="#a5b0bb"/><stop offset="1" stop-color="#56616e"/></linearGradient></defs><rect width="318" height="357" fill="url(#t1)"/></svg>
    <div class="tile-card" style="left:4px;top:138px;width:304px;height:211px">
      <div class="tile-brand">OX PANEL</div>
      <div class="tile-sub">Aluminium Panel</div>
      <p class="tile-copy">Lorem Ipsum is simply dummy text of the printing and typesetting industry.</p>
      <a class="btn btn-solid" style="position:relative;margin-top:16px;width:105px;height:30px">Shop Now</a>
    </div>
  </div>
  <div class="tile" style="left:440px;top:1209px;width:320px;height:357px">
    <svg class="fill" width="320" height="357" role="img" aria-label="Composite panel building corner against blue sky"><defs><linearGradient id="t2" x1="0" y1="0" x2="1" y2="1"><stop offset="0" stop-color="#2c49d0"/><stop offset=".45" stop-color="#4d6ae0"/><stop offset=".6" stop-color="#cfc2aa"/><stop offset="1" stop-color="#a89a82"/></linearGradient></defs><rect width="320" height="357" fill="url(#t2)"/></svg>
    <div class="tile-card" style="left:4px;top:254px;width:307px;height:97px">
      <div class="tile-brand" style="font-size:27px"><i style="background:#3a7bd5"></i>MURT PANEL</div>
    </div>
  </div>
  <div class="tile" style="left:793px;top:1209px;width:318px;height:357px">
    <svg class="fill" width="318" height="357" role="img" aria-label="Stacked coloured acrylic sheets"><defs><linearGradient id="t3" x1="0" y1="0" x2=".3" y2="1"><stop offset="0" stop-color="#2aa6e8"/><stop offset=".25" stop-color="#5fb7e6"/><stop offset=".4" stop-color="#f2601e"/><stop offset=".58" stop-color="#d81e1e"/><stop offset=".75" stop-color="#a8d83a"/><stop offset="1" stop-color="#5e8f22"/></linearGradient></defs><rect width="318" height="357" fill="url(#t3)"/></svg>
    <div class="tile-card" style="left:4px;top:254px;width:305px;height:97px">
      <div class="tile-brand" style="font-size:27px;letter-spacing:6px">TEMVORO</div>
    </div>
  </div>
  <div class="tile" style="left:89px;top:1601px;width:494px;height:303px">
    <svg class="fill" width="494" height="303" role="img" aria-label="White routed acrylic signage letters"><defs><linearGradient id="t4" x1="0" y1="0" x2="1" y2="1"><stop offset="0" stop-color="#c4c8cc"/><stop offset=".4" stop-color="#f1f2f4"/><stop offset=".7" stop-color="#dcdee1"/><stop offset="1" stop-color="#aeb2b7"/></linearGradient></defs><rect width="494" height="303" fill="url(#t4)"/></svg>
    <div class="tile-card" style="left:7px;top:197px;width:303px;height:97px"><div class="tile-name">Print and Display</div></div>
  </div>
  <div class="tile" style="left:617px;top:1601px;width:494px;height:303px">
    <svg class="fill" width="494" height="303" role="img" aria-label="LED spotlight bulbs glowing warm white"><defs><radialGradient id="t5" cx=".35" cy=".4" r=".75"><stop offset="0" stop-color="#fbe7a6"/><stop offset=".25" stop-color="#c9a45a"/><stop offset=".6" stop-color="#5e5648"/><stop offset="1" stop-color="#26222c"/></radialGradient></defs><rect width="494" height="303" fill="url(#t5)"/></svg>
    <div class="tile-card" style="left:7px;top:197px;width:303px;height:97px">
      <div class="tile-brand" style="font-size:24px;letter-spacing:1px">VESKO LED LIGHTING</div>
    </div>
  </div>
</section>

<!-- projects gallery -->
<h2 class="section-title abs" style="left:0;width:1200px;text-align:center;top:2098px">PROJECTS GALLERY</h2>
<div class="gallery-card" style="left:89px;top:2177px">
  <svg class="fill" width="324" height="291" role="img" aria-label="Modern white house at dusk"><defs><linearGradient id="g1" x1="0" y1="0" x2=".2" y2="1"><stop offset="0" stop-color="#1c48bd"/><stop offset=".3" stop-color="#5a7fd0"/><stop offset=".55" stop-color="#e3e7ee"/><stop offset=".8" stop-color="#8c95a2"/><stop offset="1" stop-color="#2e3540"/></linearGradient></defs><rect width="324" height="291" fill="url(#g1)"/></svg>
  <div class="gallery-cap">Lorem Ipsum is dummy text</div>
</div>
<div class="gallery-card" style="left:438px;top:2177px">
  <svg class="fill" width="324" height="291" role="img" aria-label="Contemporary residence under sunset sky"><defs><linearGradient id="g2" x1="0" y1="0" x2="0" y2="1"><stop offset="0" stop-color="#5f7fa6"/><stop offset=".22" stop-color="#d69a72"/><stop offset=".45" stop-color="#ece7e1"/><stop offset=".75" stop-color="#6e645a"/><stop offset="1" stop-color="#2f2b28"/></linearGradient></defs><rect width="324" height="291" fill="url(#g2)"/></svg>
  <div class="gallery-cap">Lorem Ipsum is dummy text</div>
</div>
<div class="gallery-card" style="left:788px;top:2177px">
  <svg class="fill" width="323" height="291" role="img" aria-label="Two-storey suburban house with garden"><defs><linearGradient id="g3" x1="0" y1="0" x2="0" y2="1"><stop offset="0" stop-color="#2f63c8"/><stop offset=".3" stop-color="#8fb0e0"/><stop offset=".5" stop-color="#e6e2da"/><stop offset=".78" stop-color="#7d8a6c"/><stop offset="1" stop-color="#34501f"/></linearGradient></defs><rect width="323" height="291" fill="url(#g3)"/></svg>
  <div class="gallery-cap">Lorem Ipsum is dummy text</div>
</div>
<svg class="abs" style="left:567px;top:2508px" width="66" height="28">
  <circle cx="14" cy="14" r="13" fill="#9a9a9a"/><path d="M19 14H9m4-5l-5 5 5 5" stroke="#fff" stroke-width="2.5" fill="none"/>
  <circle cx="52" cy="14" r="13" fill="#6b1141"/><path d="M47 14h10m-4-5l5 5-5 5" stroke="#fff" stroke-width="2.5" fill="none"/>
</svg>

<!-- news -->
<svg class="abs" style="left:0;top:2590px" width="1200" height="690"><defs><linearGradient id="band3" x1="0" y1="0" x2="1" y2="1"><stop offset="0" stop-color="#1b1b1f"/><stop offset="1" stop-color="#0e0e11"/></linearGradient></defs><polygon points="0,42 1200,0 1200,651 0,690" fill="url(#band3)"/></svg>
<h2 class="abs heading" style="left:0;width:1200px;text-align:center;top:2684px;font-size:29px;font-weight:600;color:var(--white)">NEWS</h2>
<article class="news-card" style="left:89px">
  <svg class="fill" width="324" height="180" role="img" aria-label="Concrete living room with fireplace"><defs><linearGradient id="n1" x1="0" y1="0" x2="0" y2="1"><stop offset="0" stop-color="#7d7b77"/><stop offset=".55" stop-color="#b0ada7"/><stop offset="1" stop-color="#d9d4cb"/></linearGradient></defs><rect width="324" height="180" fill="url(#n1)"/></svg>
  <div class="news-date">20<small>Sep, 21</small></div>
  <h3 class="news-title">Integer vitae mi in nisi sol-licitudin vulputate.</h3>
  <p class="news-copy">Lorem Ipsum is simply dummy text of the printing and...</p>
  <a class="btn btn-outline" style="left:85px;top:310px;width:102px;height:26px;font-size:10px">Read More</a>
</article>
<article class="news-card" style="left:438px">
  <svg class="fill" width="324" height="180" role="img" aria-label="Industrial kitchen with steel range hood"><defs><linearGradient id="n2" x1="0" y1="0" x2="0" y2="1"><stop offset="0" stop-color="#3c3a37"/><stop offset=".5" stop-color="#77736c"/><stop offset="1" stop-color="#4a4743"/></linearGradient></defs><rect width="324" height="180" fill="url(#n2)"/></svg>
  <div class="news-date">20<small>Sep, 21</small></div>
  <h3 class="news-title">Integer vitae mi in nisi sol-licitudin vulputate.</h3>
  <p class="news-copy">Lorem Ipsum is simply dummy text of the printing and...</p>
  <a class="btn btn-outline" style="left:85px;top:310px;width:102px;height:26px;font-size:10px">Read More</a>
</article>
<article class="news-card" style="left:788px">
  <svg class="fill" width="323" height="180" role="img" aria-label="Bright lounge with framed prints and armchair"><defs><linearGradient id="n3" x1="0" y1="0" x2="1" y2="1"><stop offset="0" stop-color="#ecebe8"/><stop offset=".6" stop-color="#cfcdc9"/><stop offset="1" stop-color="#8e8c88"/></linearGradient></defs><rect width="323" height="180" fill="url(#n3)"/></svg>
  <div class="news-date">20<small>Sep, 21</small></div>
  <h3 class="news-title">Integer vitae mi in nisi sol-licitudin vulputate.</h3>
  <p class="news-copy">Lorem Ipsum is simply dummy text of the printing and...</p>
  <a class="btn btn-outline" style="left:85px;top:310px;width:102px;height:26px;font-size:10px">Read More</a>
</article>
<svg class="abs" style="left:567px;top:3158px" width="66" height="28">
  <circle cx="14" cy="14" r="13" fill="#9a9a9a"/><path d="M19 14H9m4-5l-5 5 5 5" stroke="#222" stroke-width="2.5" fill="none"/>
  <circle cx="52" cy="14" r="13" fill="#6b1141"/><path d="M47 14h10m-4-5l5 5-5 5" stroke="#fff" stroke-width="2.5" fill="none"/>
</svg>

<!-- newsletter -->
<svg class="abs" style="left:165px;top:3333px" width="60" height="66" viewBox="0 0 60 66" fill="none" stroke="#6b1141" stroke-width="2.5">
  <path d="M4 30l26-18 26 18v30H4z"/><path d="M4 30l26 18 26-18"/><path d="M4 60l20-16M56 60L36 44"/><rect x="14" y="4" width="30" height="30" fill="#fff" transform="rotate(-15 29 19)"/><path d="M18 14h20M18 21h20M18 28h12" transform="rotate(-15 29 19)"/>
</svg>
<div class="nl-title">NEWSLETTER</div>
<p class="nl-copy">Subscribe to our newsletter and receive our updated by email.</p>
<div class="nl-form"><span>Enter email address</span>
  <a class="btn btn-solid" style="left:269px;top:3px;width:143px;height:28px">Subscribe Now</a>
</div>

<!-- footer -->
<footer class="site-footer">
  <div class="foot-brand">Brindel<span>Supplier Group</span></div>
  <div class="foot-head" style="left:353px">Quick Links</div>
  <nav class="foot-links">
    <a href="#" style="top:116px">Home</a>
    <a href="#" class="active" style="top:142px">About Us</a>
    <a href="#" style="top:168px">Projects Gallery</a>
    <a href="#" style="top:195px">News</a>
    <a href="#" style="top:222px">Contact Us</a>
  </nav>
  <div class="foot-head" style="left:574px">Address</div>
  <svg class="abs" style="left:574px;top:114px" width="16" height="20"><path d="M8 1a6 6 0 016 6c0 5-6 12-6 12S2 12 2 7a6 6 0 016-6z" fill="#fff"/><circle cx="8" cy="7" r="2.2" fill="#141417"/></svg>
  <div class="foot-info" style="top:111px">Lorem ipsum Legion L<br>qld 4209 Australia</div>
  <svg class="abs" style="left:574px;top:174px" width="16" height="16"><path d="M4 1c1 0 2 3 2 4s-1.3.8-1 2 2.5 3.5 3.5 3.5 1-1 2-1 3.5 1 3.5 2-1 2.5-2.5 2.5C6 14 1.5 9.5 1.5 4 1.5 2.3 2.8 1 4 1z" fill="#fff"/></svg>
  <div class="foot-info" style="top:172px">1300 458 903</div>
  <svg class="abs" style="left:574px;top:213px" width="16" height="12"><rect x=".5" y=".5" width="15" height="11" fill="#fff"/><path d="M1 1l7 6 7-6" stroke="#141417" stroke-width="1.3" fill="none"/></svg>
  <div class="foot-info" style="top:209px">hello@brindelgroup.example</div>
  <svg class="abs" style="left:840px;top:63px" width="271" height="169" role="img" aria-label="Location map of the office region">
    <defs><linearGradient id="mapG" x1="0" y1="0" x2="1" y2="1"><stop offset="0" stop-color="#c9dcc0"/><stop offset=".45" stop-color="#e6ead9"/><stop offset=".8" stop-color="#efe9dc"/><stop offset="1" stop-color="#b9d3e6"/></linearGradient></defs>
    <rect width="271" height="169" fill="url(#mapG)"/>
  </svg>
</footer>
<div class="copyright">Copyright © 2021 Brindel Group. All Rights Reserved</div>
<div class="social" style="left:1064px" aria-label="Social link"></div>
<div class="social" style="left:1092px;background:#111" aria-label="Social link"></div>

</body>
</html>
```